Bicycle Tour Schedule on a Business Card

Need to develop a 2 side business card that highlights a series of bike tours on 1 side and a series of events on the other side.
This will be inserted into a card wallet that attaches to a cell phone and will be handed out at an expo. The card wallets are black and red so color must coordinate with both. There is a photo of the card wallets attached.

1 side needs to be devoted to Pedal Vista Rides and the others to KRV Partners events on the other. Dates and websites are very important.

Target Market(s)

Cyclists
Predominantly men ages 40+
Educated, Professionals

Industry/Entity Type

Business

Font styles to use
Serif

Requirements
Must have
• Pedal vista rides logo on 1 side and KRV Partners logo on the other side
• dates and websites clearly visible
• Design of both sides must go together.
• Must be portrait not landscape

```html
<!DOCTYPE html>
<html lang="en">
<head>
<meta charset="utf-8">
<title>Pedal Vista Rides &amp; KRV Partners – Event Cards</title>
<link rel="stylesheet" href="https://fonts.googleapis.com/css2?family=Roboto+Condensed:wght@300;400;700&display=swap">
<style>
  :root {
    --red: #e8232a;
    --black: #0b0b0b;
    --white: #ffffff;
    --grey: #c9c9c9;
    --grey-text: #3a3a3a;
    --backdrop: #e6e4e1;
    --font: "Roboto Condensed", "Arial Narrow", sans-serif;
  }
  * { box-sizing: border-box; margin: 0; padding: 0; }
  html, body {
    width: 1200px; height: 938px; overflow: hidden;
    background: var(--backdrop);
    font-family: var(--font);
  }
  .canvas { position: relative; width: 1200px; height: 938px; }

  .card {
    position: absolute; top: 84px;
    width: 440px; height: 770px;
    overflow: hidden;
    box-shadow: 0 6px 22px rgba(0,0,0,.18);
  }
  .card--tours  { left: 120px; background: var(--black); }
  .card--events { left: 640px; background: var(--white); }

  .brand {
    position: absolute; top: 52px; right: 34px;
    display: flex; align-items: center; gap: 10px;
    font-family: var(--font); font-weight: 700;
    font-size: 30px; letter-spacing: .5px; text-transform: uppercase;
  }
  .card--tours .brand  { color: var(--white); }
  .card--events .brand { color: var(--red); font-size: 26px; }
  .brand__dot { width: 22px; height: 22px; border-radius: 50%; background: var(--red); }
  .brand__square { width: 40px; height: 40px; background: var(--red); }

  .stripes {
    position: absolute; left: -300px; width: 1100px;
    transform: rotate(-24deg); transform-origin: 0 0;
  }
  .card--tours .stripes  { top: 473px; }
  .card--events .stripes { top: 423px; }

  .band {
    display: flex; flex-direction: column; justify-content: center;
    color: var(--white);
    text-transform: uppercase; line-height: 1.05;
  }
  .band__text { width: var(--w); text-align: center; }
  .band + .band { margin-top: 6px; }
  .card--tours .band { background: var(--red); height: 64px; }

  .band__title { font-weight: 700; font-size: 28px; display: block; }
  .band__title--small { font-weight: 400; font-size: 21px; }
  .band__date { font-weight: 400; font-size: 23px; display: block; }
  .band__date--small { font-size: 17px; }
  .band__tag { font-weight: 400; font-size: 14px; display: block; letter-spacing: .3px; }
  .band__lead { font-weight: 700; font-size: 24px; display: block; }

  .card--events .band { height: 62px; background: var(--red); }
  .card--events .band + .band { margin-top: 5px; }
  .card--events .band--series {
    background: var(--black); height: 46px; margin-top: 0;
  }
  .card--events .band--series + .band--sub { margin-top: 0; }
  .card--events .band--sub {
    background: var(--grey); color: var(--grey-text); height: 50px;
  }
  .series-name { font-weight: 400; font-size: 26px; letter-spacing: .5px; }
  .series-sub  { font-weight: 300; font-size: 19px; }
  .event-name  { font-weight: 700; font-size: 27px; display: block; }
  .event-name--small { font-weight: 400; font-size: 17px; }
  .event-info  { font-weight: 400; font-size: 15px; display: block; letter-spacing: .3px; }
</style>
</head>
<body>
<main class="canvas">

  <section class="card card--tours" aria-label="Pedal Vista Rides tour schedule">
    <div class="brand"><span class="brand__dot"></span>Pedal Vista Rides</div>
    <div class="stripes">
      <div class="band"><p class="band__text" style="--w:1110px">
        <span class="band__lead">Fully Supported Bike Tours</span>
        <span class="band__tag">Discover the hidden gems on two wheels</span></p></div>
      <div class="band"><p class="band__text" style="--w:1046px">
        <span class="band__title">Heart of Colorado</span>
        <span class="band__date">June 26 - July 2, 2016</span></p></div>
      <div class="band"><p class="band__text" style="--w:984px">
        <span class="band__title band__title--small">Colorado Front Range Tour</span>
        <span class="band__date">August 14-20, 2016</span></p></div>
      <div class="band"><p class="band__text" style="--w:922px">
        <span class="band__title">Cape Cod Tour</span>
        <span class="band__date">October 9-15, 2016</span></p></div>
      <div class="band"><p class="band__text" style="--w:860px">
        <span class="band__title band__title--small">Florida Keys Tour</span>
        <span class="band__date band__date--small">November 6-12 &amp; December 4-10, 2016</span></p></div>
    </div>
  </section>

  <section class="card card--events" aria-label="KRV Partners event schedule">
    <div class="brand"><span class="brand__square"></span>KRV Partners</div>
    <div class="stripes">
      <div class="band band--series"><p class="band__text series-name" style="--w:1118px">Tri Cadence Series:</p></div>
      <div class="band band--sub"><p class="band__text series-sub" style="--w:1074px">Cycling camps for youth</p></div>
      <div class="band"><p class="band__text" style="--w:1020px">
        <span class="event-name">Mountain Bike Camp</span>
        <span class="event-info">July 8-10, 2016</span></p></div>
      <div class="band"><p class="band__text" style="--w:960px">
        <span class="event-name">Cyclocross Camp</span>
        <span class="event-info">Aug 26-28, 2016 tricadenceseries.org</span></p></div>
      <div class="band"><p class="band__text" style="--w:900px">
        <span class="event-name">Mile High Hundred Ride</span>
        <span class="event-info">June 18, 2016 milehighhundred.com</span></p></div>
      <div class="band"><p class="band__text" style="--w:842px">
        <span class="event-name event-name--small">Foothill Loop Challenge</span>
        <span class="event-info">July 30, 2016 foothillloop.com</span></p></div>
      <div class="band"><p class="band__text" style="--w:782px">
        <span class="event-name">Goofy Wheel Ride</span>
        <span class="event-info">September 11, 2016 goofywheelride.com</span></p></div>
    </div>
  </section>

</main>
</body>
</html>
```